BRM Going Cashless

Hello,
We are a medical office looking to get a flyer created to promote to our patients we will be going "Cashless." Our tagline will be "Cash-Less is Stress-Less"

"Starting in July, to offer you the fastest and most convenient service, we are transitioning to a cashless system. You can now enjoy faster checkout times and greater security with card and contactless payments. More info to come."

I've added two other flyers as sample designs we've used.

Please include logo, addresses, website, phone number

Files to include jpeg, png, pdf (under 5mb), Facebook and Instagram sizing.

Thank you,
Marlo

```html
<!DOCTYPE html>
<html lang="en">
<head>
<meta charset="utf-8">
<title>BRM Going Cashless</title>
<link href="https://fonts.googleapis.com/css2?family=Oswald:wght@500;600&family=Cabin:wght@600&family=Cinzel:wght@600&family=Roboto+Slab:wght@400;500&family=Merriweather:ital,wght@1,700&display=swap" rel="stylesheet">
<style>
  :root {
    --stage: #58585a;
    --header: #2e2e2e;
    --orange: #f47c47;
    --teal: #55c2a7;
    --ink: #2b2b2e;
    --navy: #22222f;
    --paper: #f7f8fa;
    --ring: #f6e6dc;
  }
  * { margin: 0; padding: 0; box-sizing: border-box; }
  html, body { width: 1200px; height: 846px; overflow: hidden; background: var(--stage); }
  .flyer {
    position: absolute; left: 300px; top: 34px; width: 600px; height: 778px;
    background: radial-gradient(ellipse at 85% 40%, #e9ebef 0%, var(--paper) 45%, #ffffff 100%);
    overflow: hidden; color: var(--ink);
  }
  .header {
    position: absolute; left: 0; top: 0; width: 600px; height: 156px;
    background: var(--header);
    display: flex; align-items: center; justify-content: center; gap: 14px;
  }
  .brand-dot { width: 22px; height: 22px; border-radius: 50%; background: var(--teal); }
  .brand-name {
    font-family: "Oswald", sans-serif; font-weight: 600; font-size: 34px;
    color: var(--orange); letter-spacing: 1px; text-transform: uppercase;
  }
  .center { position: absolute; left: 0; width: 600px; text-align: center; }
  .headline {
    top: 172px; font-family: "Oswald", sans-serif; font-weight: 600;
    font-size: 70px; line-height: 80px; color: var(--orange); letter-spacing: 1px;
  }
  .tagline {
    top: 252px; font-family: "Cabin", sans-serif; font-weight: 600;
    font-size: 35px; line-height: 42px; color: var(--teal);
  }
  .start-date {
    top: 304px; font-family: "Cinzel", serif; font-weight: 600;
    font-size: 33px; line-height: 40px; color: var(--ink);
  }
  .intro {
    top: 352px; font-family: "Roboto Slab", serif; font-weight: 500;
    font-size: 19px; line-height: 25px; color: var(--ink);
  }
  .photo {
    position: absolute; top: 440px; width: 178px; height: 178px; border-radius: 50%;
    border: 5px solid var(--ring); box-shadow: 0 2px 6px rgba(0,0,0,.15);
  }
  .photo-exam { left: 25px; background: linear-gradient(135deg, #eef0f2, #d9c2b0 60%, #5f7580); }
  .photo-office { left: 212px; background: linear-gradient(180deg, #cfe0ef 0%, #9b4a3a 35%, #7c3a2e 60%, #6f9a45 85%, #c9c2b6 100%); }
  .photo-treatment { left: 399px; background: linear-gradient(135deg, #f2f2f4, #8a8fe0 55%, #e4c2a8); }
  .benefits {
    top: 638px; font-family: "Roboto Slab", serif; font-weight: 400;
    font-size: 15px; line-height: 19px; color: var(--navy);
  }
  .phone {
    position: absolute; left: 37px; top: 686px; font-family: "Oswald", sans-serif;
    font-weight: 500; font-size: 38px; line-height: 44px; color: var(--navy);
  }
  .website {
    position: absolute; left: 39px; top: 731px; font-family: "Roboto Slab", serif;
    font-weight: 500; font-size: 17px; letter-spacing: 2px; color: var(--navy);
  }
  .more-info {
    position: absolute; left: 344px; top: 696px; font-family: "Merriweather", serif;
    font-style: italic; font-weight: 700; font-size: 15px; color: var(--navy);
  }
  .more-info-bar {
    position: absolute; left: 483px; top: 706px; width: 117px; height: 7px; background: var(--orange);
  }
  .address {
    position: absolute; left: 344px; top: 722px; font-family: "Roboto Slab", serif;
    font-size: 13px; line-height: 18px; color: var(--navy);
  }
  .footer-band { position: absolute; left: 0; bottom: 0; width: 600px; height: 12px; background: var(--teal); }
</style>
</head>
<body>
  <main class="flyer">
    <header class="header">
      <span class="brand-dot"></span>
      <span class="brand-name">BRM Foot &amp; Ankle</span>
    </header>

    <h1 class="center headline">CASHLESS</h1>
    <p class="center tagline">Cash-Less is Stress-Less</p>
    <p class="center start-date">STARTING IN JULY</p>
    <p class="center intro">to offer you the fastest and most<br>convenient service, we are transitioning<br>to a cashless system.</p>

    <div class="photo photo-exam" role="img" aria-label="Podiatrist examining a patient's foot"></div>
    <div class="photo photo-office" role="img" aria-label="Brick clinic building entrance"></div>
    <div class="photo photo-treatment" role="img" aria-label="Gloved hands treating a patient's toes"></div>

    <p class="center benefits">You can now enjoy faster checkout times and greater<br>security with card and contactless payments.</p>

    <p class="phone">(877)555-0142</p>
    <p class="website">www.brmfootcare.com</p>

    <p class="more-info">More info to come</p>
    <span class="more-info-bar"></span>
    <p class="address">58 Orchard Ridge Dr.,<br>Ste 210, Westbrook, MD 21090</p>

    <div class="footer-band"></div>
  </main>
</body>
</html>
```